Basic Commercial & Residential Real Estate Web Site

I need a basic website for a new real estate company that deals with both residential and commercial sales. It must be clean and professional. We sell homes, office buildings, farms, and ranches. It should feel crisp and clean.
I need a main page with my logo and links to commercial, residential, farm and land searches with contact data forms. Also incorporated would be a mls property search (IDX) form. I am in Northern California and the current site I posted is at www.tqvandel.com. I need the functionality of the links and the supporting pages. I do not have all the copy ready because I did not know what to expect.
Updates

Project Deadline Extended
Reason: I apologize, I am extremely busy and you all need more data to do a good job. All the designs are great so far and it is extremely difficult to choose at this point. I haven't given you enough data. I haver now uploaded some relevent photos (not very good) and edited the brief. I am looking for what I call the Landing or main page with some functionality built in to other pages which I also need. Example if you click on "Commercial" it should go to a page that discusses our commercial dept.......

I would like to thank all the designers for all their hard work and efforts, I wish I could reward you all.

Thanks again for your creative and professional designs.

Gareth

Target Market(s)

Corporate Execs for the Commercial Buildings
Homeowners/Families for the Homes and Farms
Upper end people for the land to build estates

Industry/Entity Type

Real Estate

Font styles to use
Sans Serif

Requirements
Must have
• Our Logo should be prominent, pronounced
Need contact data or button
Functional Page that links to other data pages
Must Have a "search for properties" feature
Must say "Commercial and Residential Representation"
Pictures of Commercial Building and Nice Home (Tradtional not contemporary)
Nice to have
• Individual Buttons or links to "Commercial, Residential, Farm/Ranch, Land"
Contact Data displayed
button that says "Maple Crest"-next to button is Maple Crest Logo-see www.maplecrestvale.bz
Links to "Buyers and "Sellers"
Links to Facebook, twitter,.....etc
Should not have
• 20+ story commercial buildings or ultra modern. See uploaded files of typical buildings for commercial.

```html
<!DOCTYPE html>
<html lang="en">
<head>
<meta charset="utf-8">
<title>Properties by Vandel</title>
<link href="https://fonts.googleapis.com/css2?family=Open+Sans:wght@400;600;700&family=Arimo:wght@400;700&display=swap" rel="stylesheet">
<style>
:root{
  --black:#000;
  --white:#fff;
  --side:#cfcfcf;
  --accent:#3fb8ea;
  --text:#111;
  --muted:#555;
  --field:#e6e6e6;
  --hero-dusk:#2a4a86;
  --hero-warm:#c79a6a;
}
*{box-sizing:border-box;margin:0;padding:0}
html,body{width:1000px;height:1200px;overflow:hidden}
body{background:var(--side);font-family:"Arimo",Arial,sans-serif;color:var(--text);position:relative}
.page{position:absolute;left:110px;top:0;width:780px;height:1200px;background:var(--white)}
/* header */
.site-header{height:70px;background:var(--black);display:flex;align-items:flex-end;padding:0 18px 12px 18px;position:relative;font-family:"Open Sans",sans-serif;color:var(--white)}
.brand{display:flex;flex-direction:column;line-height:1;margin-right:28px;font-weight:400}
.brand-small{font-size:10px;letter-spacing:1px;margin-left:22px}
.brand-name{font-size:34px;letter-spacing:1px}
.main-nav{display:flex;gap:18px;font-size:12px;margin-bottom:4px}
.main-nav span::after{content:" ▾";font-size:9px}
.utility{position:absolute;right:18px;top:10px;text-align:right;font-size:11px}
.utility .links{display:flex;gap:18px;justify-content:flex-end}
.phone{margin-top:14px;color:var(--accent);font-size:14px;display:flex;align-items:center;gap:5px;justify-content:flex-end}
/* hero */
.hero-wide{position:absolute;left:0;top:70px;width:1000px;height:290px;background:linear-gradient(90deg,#5b6470,#3b4654 30%,#3b4654 70%,#3d4a3f)}
.hero{position:absolute;left:110px;top:70px;width:780px;height:290px;background:radial-gradient(ellipse at 55% 65%,var(--hero-warm),#6e5a48 40%,var(--hero-dusk) 80%)}
.arrow{position:absolute;top:120px;color:var(--white);font-size:38px;font-family:"Open Sans",sans-serif}
/* search */
.search{position:absolute;top:360px;left:0;width:780px;height:46px;background:var(--black);display:flex;align-items:center;justify-content:center;gap:8px;font-family:"Open Sans",sans-serif}
.search-label{color:var(--accent);font-size:15px;margin-right:6px}
.select{width:92px;height:18px;background:var(--field);font-size:10px;color:#999;padding:3px 5px;position:relative}
.select::after{content:"▾";position:absolute;right:3px;top:2px;color:#777}
.go{width:34px;height:18px;background:var(--accent)}
/* intro */
.intro{position:absolute;top:420px;left:60px;width:660px;text-align:center}
.intro-brand{font-family:"Open Sans",sans-serif;line-height:1;display:inline-flex;flex-direction:column;color:var(--black)}
.intro-brand .brand-small{font-size:7px;margin-left:14px}
.intro-brand .brand-name{font-size:24px}
.lead{font-size:15px;margin:16px 0 12px;line-height:1.35}
.body-copy{font-size:11px;font-weight:700;color:var(--muted);line-height:1.45;text-align:left;margin-bottom:10px}
/* listings */
.section-bar{position:absolute;top:620px;left:14px;width:752px;height:30px;background:var(--black);color:var(--white);font-family:"Open Sans",sans-serif;font-weight:600;font-size:14px;padding:6px 12px}
.grid{position:absolute;top:660px;left:14px;width:752px;height:340px}
.tile{position:absolute;overflow:hidden}
.t-sky{background:linear-gradient(180deg,#4f8fd0,#7fae66 70%,#5a6b3e)}
.t-warm{background:linear-gradient(180deg,#6d8fb8,#b59a72 60%,#6e5a3f)}
.t-white{background:linear-gradient(180deg,#7ea8d8,#e9e4dc 55%,#a79d8e)}
.t-hill{background:linear-gradient(180deg,#9bb8d6,#8d9a78 55%,#6b6a55)}
.caption{position:absolute;left:10px;bottom:12px;background:rgba(0,0,0,.7);color:var(--white);padding:6px 10px;width:170px}
.caption h3{font-size:11px;font-weight:400}
.caption p{font-size:8px;color:#ccc;margin:2px 0}
.caption strong{font-size:13px}
.ribbon{position:absolute;top:-4px;left:-24px;width:120px;transform:rotate(-40deg) translate(-6px,22px);background:#1e5fb3;color:var(--white);font-family:"Open Sans",sans-serif;font-weight:700;font-size:9px;text-align:center;padding:3px 0}
/* testimonial */
.testimonial{position:absolute;top:1010px;left:40px;width:700px;height:80px;text-align:center}
.testimonial .nav{position:absolute;top:22px;color:#aaa;font-size:24px}
.quote-mark{position:absolute;font-family:Georgia,serif;color:#ccc;font-size:44px}
.testimonial p{font-size:10px;font-weight:700;color:var(--muted);margin:6px 120px 6px;line-height:1.4}
.testimonial cite{font-size:11px;font-weight:700;font-style:italic}
.band{position:absolute;top:1102px;left:0;width:1000px;height:16px;background:var(--accent)}
.band-page{position:absolute;top:1102px;left:0;width:780px;height:16px;background:var(--accent)}
/* footer */
.site-footer{position:absolute;top:1118px;left:0;width:780px;height:82px;background:var(--black);color:var(--white);display:flex;gap:60px;padding:10px 20px;font-size:8px;line-height:1.5}
.site-footer h4{font-size:9px;font-weight:400;margin-bottom:4px}
.footer-links{display:grid;grid-template-columns:auto auto;column-gap:30px}
.social{display:flex;gap:5px}
.social span{width:16px;height:16px;display:block}
.footer-brand{position:absolute;right:20px;bottom:8px;font-family:"Open Sans",sans-serif;line-height:1;display:flex;flex-direction:column}
.footer-brand .brand-small{font-size:5px;margin-left:8px}
.footer-brand .brand-name{font-size:14px}
</style>
</head>
<body>
<div class="hero-wide" role="img" aria-label="Dimmed continuation of the slideshow photo"></div>
<div class="band"></div>
<main class="page">
  <header class="site-header">
    <div class="brand"><span class="brand-small">PROPERTIES BY</span><span class="brand-name">VANDEL</span></div>
    <nav class="main-nav"><span>Commercial</span><span>Residential</span><span>Farm</span><span>Vacant Land</span></nav>
    <div class="utility">
      <div class="links"><span>About Us</span><span>Contact Us</span></div>
      <div class="phone"><svg width="11" height="11" viewBox="0 0 12 12"><path d="M2 1h3l1 3-2 1a7 7 0 0 0 3 3l1-2 3 1v3c-6 1-10-3-9-9z" fill="#3fb8ea"/></svg>(530) 555-0148</div>
    </div>
  </header>
</main>
<div class="hero" role="img" aria-label="Evening photo of a traditional stucco villa with arched balconies and a lit spa"></div>
<main class="page" style="top:0;background:transparent;pointer-events:none">
  <span class="arrow" style="left:10px;top:190px">‹</span>
  <span class="arrow" style="right:10px;top:190px">›</span>
  <form class="search">
    <span class="search-label">Property Search</span>
    <span class="select">All Locations</span><span class="select" style="width:60px">All Types</span><span class="select" style="width:60px">All Beds</span><span class="select" style="width:60px">All Prices</span><span class="go"></span>
  </form>
  <section class="intro">
    <div class="intro-brand"><span class="brand-small">PROPERTIES BY</span><span class="brand-name">VANDEL</span></div>
    <p class="lead">Lorem ipsum dolor sit amet, consectetur adipiscing elit. Etiam quis tellus odio. Lorem ipsum dolor sit amet, consectetur adipiscing elit.</p>
    <p class="body-copy">Praesent commodo bibendum euismod. Integer at neque iaculis, dictum mauris vitae, commodo justo. Class aptent taciti sociosqu ad litora torquent per conubia nostra, per inceptos himenaeos. Suspendisse consequat dui sem, a ultricies odio pretium quis. Donec viverra mattis tellus, eget scelerisque velit vestibulum nec.</p>
    <p class="body-copy">Suspendisse vitae pulvinar nunc, vel pretium ligula. Aliquam eu porttitor massa. Aliquam adipiscing, neque tristique gravida pellentesque, massa ante porttitor erat, id sollicitudin orci erat ac mauris. Nunc ut est vel lorem laoreet sodales.</p>
  </section>
  <h2 class="section-bar">Recently Added Property</h2>
  <section class="grid">
    <div class="tile t-sky" style="left:0;top:0;width:492px;height:190px" role="img" aria-label="Suburban home behind tall pines">
      <div class="caption"><h3>Lorem ipsum dolor sit amet</h3><p>Suspendisse vitae pulvinar nunc</p><strong>$1,725,000</strong></div>
    </div>
    <div class="tile t-warm" style="left:502px;top:0;width:250px;height:92px" role="img" aria-label="Courtyard home with garden"><div class="ribbon">PRICE REDUCED</div></div>
    <div class="tile t-sky" style="left:502px;top:98px;width:250px;height:92px" role="img" aria-label="House among palm trees"></div>
    <div class="tile t-hill" style="left:0;top:200px;width:250px;height:65px" role="img" aria-label="Open land with hills"></div>
    <div class="tile t-hill" style="left:0;top:271px;width:250px;height:69px" role="img" aria-label="Land parcel with sign"><div class="ribbon">PRICE REDUCED</div></div>
    <div class="tile t-white" style="left:260px;top:200px;width:492px;height:140px" role="img" aria-label="White Spanish style home with columns">
      <div class="caption"><h3>Lorem ipsum dolor sit amet</h3><p>Suspendisse vitae pulvinar nunc</p><strong>$1,725,000</strong></div>
    </div>
  </section>
  <blockquote class="testimonial">
    <span class="nav" style="left:0">‹</span><span class="nav" style="right:0">›</span>
    <span class="quote-mark" style="left:90px;top:-14px">“</span>
    <p>Suspendisse vitae pulvinar nunc, vel pretium ligula. Aliquam eu porttitor massa. Aliquam adipiscing, neque tristique gravida pellentesque, massa ante porttitor erat, id sollicitudin orci.</p>
    <cite>Sam Ortega - California</cite>
    <span class="quote-mark" style="right:90px;top:44px">”</span>
  </blockquote>
  <div class="band-page"></div>
  <footer class="site-footer">
    <div><h4>Contact Information</h4>PROPERTIES BY VANDEL<br>2150 Orchard Row Drive<br>Maple Valley, CA 95000<br>(530) 555-0148</div>
    <div><h4>Useful Links</h4><div class="footer-links"><span>Home</span><span>Commercial</span><span>About Us</span><span>Residential</span><span>Contact Us</span><span>Farm</span><span>Testimonials</span><span>Vacant Land</span></div></div>
    <div><h4>Connect with us</h4><div class="social"><span style="background:#3b5998"></span><span style="background:#2aa9e0"></span><span style="background:#d34836"></span><span style="background:#c8232c"></span></div></div>
    <div class="footer-brand"><span class="brand-small">PROPERTIES BY</span><span class="brand-name">VANDEL</span></div>
  </footer>
</main>
</body>
</html>
```